QuartzNook Works, LLC Corporate Web Site

The goal of this web site is simple. To provide an information and corporate information site for people who click on company links from other web sites. Put simply, this web site is primarily a brochure web site for the parent business. It will contain information about the company and our products with links to those products. It will be designed as a small web site but scalable as we add more products and services to our repertoire.

Please see the PDF in the uploaded files/media for more information on colors and basic guidelines, but be creative for sure.

Target Market(s)

General

Industry/Entity Type

Technology, Software

Coding

Coded - Design and coding required

Font styles to use
Other font styles liked:
• Goliath, Roboto

Colors
FFC000
F8CF3A
FAE287
FDF2CF
FEFAEE

Requirements
Must have
• Home page template, interior template, News/Press release template
Nice to have
• Searchable
Should not have
• carousels, one-page design

```html
<!DOCTYPE html>
<html lang="en">
<head>
<meta charset="utf-8">
<title>QuartzNook Works, LLC – Mobile App Solutions</title>
<link href="https://fonts.googleapis.com/css2?family=Poppins:wght@300;400;500;600;700&display=swap" rel="stylesheet">
<style>
:root{
  --orange:#f8a020;
  --orange-soft:#fbc25e;
  --lavender:#7c80c6;
  --lavender-soft:#eceefa;
  --ink:#111322;
  --body:#5d5f6e;
  --muted:#8a8c99;
  --line:#e3e4ee;
  --white:#ffffff;
}
*{box-sizing:border-box;margin:0;padding:0}
html,body{width:1200px;height:3662px;overflow:hidden;background:var(--white)}
body{font-family:"Poppins",sans-serif;color:var(--ink)}
.page{position:relative;width:1200px;height:3662px;overflow:hidden}
.abs{position:absolute}
a{color:inherit;text-decoration:none}

/* header */
.hero-bg{left:0;top:0;width:1200px;height:500px;background:linear-gradient(180deg,#eef0fb 0%,#e9ebf8 70%,#f3f4fc 100%)}
.hero-wave{left:0;top:380px;width:1200px;height:160px}
.brand{left:125px;top:22px;font-size:22px;font-weight:700;color:var(--orange);letter-spacing:.5px;line-height:1}
.brand small{display:block;font-size:8px;letter-spacing:4px;color:var(--lavender);font-weight:500;margin-top:3px;padding-left:34px}
.nav a{position:absolute;top:32px;font-size:14px;color:#33354a}
.phone{left:836px;top:32px;font-size:14px;color:#2c2e40;display:flex;align-items:center;gap:8px}
.btn{display:flex;align-items:center;justify-content:center;background:var(--orange);color:#fff;font-weight:500;border-radius:22px;box-shadow:0 6px 14px rgba(248,160,32,.35)}
.btn-contact{left:977px;top:23px;width:126px;height:38px;font-size:15px}

/* hero */
.hero-kicker{left:121px;top:178px;font-size:46px;font-weight:600;color:var(--lavender);line-height:1.2}
.hero-title{left:121px;top:235px;font-size:46px;font-weight:600;color:var(--ink);line-height:1.2}
.hero-lead{left:121px;top:306px;width:400px;font-size:14px;line-height:20px;color:var(--body)}
.btn-apply-hero{left:121px;top:381px;width:124px;height:36px;font-size:15px}
.hero-art{left:626px;top:100px;width:454px;height:390px;border-radius:30px;background:radial-gradient(circle at 55% 55%,#fbd08a 0%,#f6c374 30%,#dfe1f4 62%,rgba(236,238,250,0) 75%)}
.chat-bubble{left:975px;top:387px;width:158px;height:54px;background:#fff;border-radius:10px;box-shadow:0 4px 14px rgba(90,95,160,.15);display:flex;align-items:center;gap:8px;padding:0 10px;font-size:13px;line-height:15px;color:#3a3c50}
.chat-bubble i{display:block;width:30px;height:30px;border-radius:50%;border:2px solid var(--lavender);flex:none}
.chat-btn{left:1088px;top:451px;width:40px;height:40px;border-radius:50%;background:var(--lavender);display:flex;align-items:center;justify-content:center}

/* section headings */
.eyebrow{font-size:12px;font-weight:600;letter-spacing:2px;color:var(--orange);text-transform:uppercase}
.center{left:0;width:1200px;text-align:center}
.h2{font-size:28px;font-weight:600;color:var(--ink)}

/* products */
.products-band{left:0;top:768px;width:1200px;height:240px;background:linear-gradient(180deg,rgba(236,238,250,0) 0%,#e6e8f5 50%,rgba(236,238,250,0) 100%)}
.product{top:718px;width:220px;height:211px;background:#fff;border-radius:4px;box-shadow:0 4px 18px rgba(80,85,140,.06);text-align:center}
.product .ico{position:absolute;left:82px;top:-3px;width:56px;height:64px}
.product h3{position:absolute;top:74px;left:0;width:100%;font-size:15px;font-weight:500}
.product p{position:absolute;top:104px;left:20px;width:180px;font-size:11.5px;line-height:17px;color:var(--muted)}
.learn{font-size:12px;color:var(--orange);border-bottom:1px solid var(--orange);padding-bottom:2px}
.product .learn{position:absolute;top:170px;left:50%;transform:translateX(-50%);white-space:nowrap}

/* why */
.why-art{left:50px;top:1030px;width:462px;height:463px;border-radius:50% 50% 46% 54%/40% 40% 60% 60%;background:linear-gradient(160deg,#e3e5f2 0%,#f2f2f6 60%,#f7dcae 100%)}
.why-eyebrow{left:606px;top:1109px}
.why-title{left:606px;top:1133px}
.why-lead{left:606px;top:1180px;width:400px;font-size:14px;line-height:20px;color:var(--body)}
.why-list{left:606px;top:1250px;width:390px;list-style:none}
.why-list li{position:relative;padding-left:32px;font-size:13.5px;line-height:20px;color:#1d1f30;font-weight:500}
.why-list li svg{position:absolute;left:0;top:1px}
.why-list li+li{margin-top:19px}

/* how */
.how-eyebrow{top:1604px}
.how-title{top:1628px}
.how-path{left:0;top:1700px;width:1200px;height:200px}
.step{top:1700px;width:220px;text-align:center}
.step .ico{width:48px;height:48px;margin:0 auto;border-radius:50%;background:#fff;box-shadow:0 3px 10px rgba(80,85,140,.12);display:flex;align-items:center;justify-content:center}
.step .ico span{width:24px;height:22px;border-radius:5px}
.step h3{margin-top:19px;font-size:15px;font-weight:600}
.step p{margin-top:10px;font-size:12px;line-height:18px;color:var(--muted)}
.btn-apply-how{left:539px;top:1878px;width:124px;height:37px;font-size:15px}

/* projects */
.projects-band{left:0;top:1976px;width:1200px;height:630px;background:linear-gradient(180deg,#ffffff 0%,#eceefa 25%,#e8eaf7 70%,#ffffff 100%)}
.projects-eyebrow{left:135px;top:2042px}
.projects-title{left:135px;top:2066px}
.project{top:2134px;width:290px;height:363px;background:#fff;border-radius:4px;box-shadow:0 4px 18px rgba(80,85,140,.06)}
.project .shot{position:absolute;left:20px;top:21px;width:250px;height:152px}
.project h3{position:absolute;left:20px;top:196px;font-size:20px;font-weight:600}
.project .tag{position:absolute;left:20px;top:229px;font-size:11px;letter-spacing:1.5px;color:var(--muted)}
.project p{position:absolute;left:20px;top:257px;width:250px;font-size:11.5px;line-height:17px;color:var(--body);white-space:nowrap;overflow:hidden;text-overflow:ellipsis}
.project p+p{top:274px}
.project .learn{position:absolute;left:20px;top:314px}

/* testimonials */
.t-eyebrow{top:2624px}
.t-title{top:2647px}
.quote{top:2752px;width:400px}
.quote .stars{display:flex;gap:4px}
.quote .client{position:absolute;top:-6px;font-size:13px;font-weight:700;color:#2f3142;display:flex;align-items:center;gap:6px}
.quote .client i{display:block;width:16px;height:16px;border-radius:50%;background:#8c6bb1}
.quote blockquote{margin-top:26px;font-size:14px;line-height:21.5px;color:var(--body);font-weight:300}
.person{position:absolute;top:150px;left:24px;display:flex;gap:14px;align-items:flex-start}
.person i{display:block;width:30px;height:30px;border-radius:50%;background:linear-gradient(#bfc0c6 0 45%,#8e9099 45%)}
.person b{display:block;font-size:15px;font-weight:600;color:var(--ink);line-height:20px}
.person span{display:block;font-size:11.5px;color:var(--muted);line-height:16px}

/* cta */
.cta-band{left:0;top:3084px;width:1200px;height:186px;background:linear-gradient(90deg,#ffffff,#eceefa 20%,#eceefa 80%,#ffffff)}
.cta-box{left:186px;top:3061px;width:826px;height:216px;border:3px solid #9a9dd4;border-radius:26px;background:linear-gradient(180deg,#f1f2f7,#e9eaf2);box-shadow:0 8px 24px rgba(90,95,160,.12)}
.cta-gears{left:960px;top:3026px;width:96px;height:92px;border-radius:40%;background:radial-gradient(circle at 68% 62%,var(--orange) 0 26%,transparent 27%),radial-gradient(circle at 22% 22%,#9fa2cc 0 20%,transparent 21%)}
.cta-title{left:186px;top:3110px;width:826px;text-align:center;font-size:27px;font-weight:600;line-height:37px}
.cta-title em{font-style:normal;color:var(--lavender)}
.btn-apply-cta{left:539px;top:3200px;width:124px;height:37px;font-size:15px}

/* footer */
.foot-brand{left:159px;top:3360px;font-size:34px;font-weight:700;color:var(--orange);line-height:1}
.foot-brand small{display:block;font-size:11px;letter-spacing:6px;color:var(--lavender);font-weight:500;margin-top:4px;padding-left:64px}
.foot-about{left:159px;top:3443px;width:220px;font-size:12px;line-height:17px;color:var(--body)}
.foot-about a{color:var(--lavender);font-weight:500}
.foot-h{font-size:18px;font-weight:500;color:var(--ink);top:3361px}
.foot-links{left:506px;top:3401px;list-style:none}
.foot-links li{font-size:13.5px;color:#3b3d50;line-height:18px}
.foot-links li+li{margin-top:15.5px}
.contact-list{left:704px;top:3402px;list-style:none;width:180px}
.contact-list li{position:relative;padding-left:22px;font-size:13.5px;line-height:20px;color:#3b3d50}
.contact-list li svg{position:absolute;left:0;top:4px}
.contact-list li+li{margin-top:10px}
.socials{left:924px;top:3398px;display:flex;gap:9px}
.socials span{display:block;width:22px;height:22px;border-radius:3px;background:var(--lavender)}
.to-top{left:1008px;top:3522px;width:43px;height:43px;border-radius:50%;background:var(--lavender);box-shadow:0 4px 10px rgba(90,95,160,.3);display:flex;align-items:center;justify-content:center}
.foot-rule{left:159px;top:3602px;width:882px;height:1px;background:var(--line)}
.copyright{top:3624px;font-size:13px;color:var(--muted)}
</style>
</head>
<body>
<div class="page">

  <!-- header + hero -->
  <div class="abs hero-bg"></div>
  <svg class="abs hero-wave" viewBox="0 0 1200 160" preserveAspectRatio="none" aria-hidden="true">
    <path d="M0 60 C300 140 700 150 1200 20 L1200 160 L0 160 Z" fill="#ffffff"/>
  </svg>

  <div class="abs brand">QuartzNook<small>WORKS</small></div>
  <nav class="nav">
    <a style="left:307px">About</a>
    <a style="left:383px">Products</a>
    <a style="left:478px">Projects</a>
    <a style="left:566px">Contributions</a>
    <a style="left:693px">News</a>
  </nav>
  <div class="abs phone">
    <svg width="14" height="14" viewBox="0 0 24 24"><path d="M6.6 10.8a15 15 0 006.6 6.6l2.2-2.2a1 1 0 011-.25 11.4 11.4 0 003.6.57 1 1 0 011 1V20a1 1 0 01-1 1A17 17 0 013 4a1 1 0 011-1h3.5a1 1 0 011 1c0 1.25.2 2.45.57 3.57a1 1 0 01-.25 1z" fill="var(--orange)"/></svg>
    555-014-2276
  </div>
  <a class="abs btn btn-contact">Contact Us</a>

  <div class="abs hero-kicker">Empowering</div>
  <h1 class="abs hero-title">Your Digital Vision</h1>
  <p class="abs hero-lead">Crafting Innovative Mobile Experiences to Connect and Inspire in a Rapidly Evolving World</p>
  <a class="abs btn btn-apply-hero">Apply Now</a>
  <div class="abs hero-art" role="img" aria-label="Isometric illustration of a smartphone with floating app screens, map, calendar and gears"></div>
  <div class="abs chat-bubble"><i></i><span>Hi there, have a question?</span></div>
  <div class="abs chat-btn">
    <svg width="18" height="18" viewBox="0 0 24 24"><path d="M12 3C6.5 3 2 6.8 2 11.5c0 2.3 1.1 4.4 2.9 5.9L4 21l4.2-2.1c1.2.4 2.5.6 3.8.6 5.5 0 10-3.8 10-8.5S17.5 3 12 3z" fill="#fff"/><circle cx="8" cy="11.5" r="1.2" fill="var(--lavender)"/><circle cx="12" cy="11.5" r="1.2" fill="var(--lavender)"/><circle cx="16" cy="11.5" r="1.2" fill="var(--lavender)"/></svg>
  </div>

  <!-- products -->
  <div class="abs eyebrow center" style="top:595px">Our Products</div>
  <h2 class="abs h2 center" style="top:618px">Mobile App Solutions</h2>
  <div class="abs products-band"></div>

  <article class="abs product" style="left:135px">
    <div class="ico" role="img" aria-label="Phone with code icon" style="background:linear-gradient(135deg,#8f93d3,#f8b54a)"></div>
    <h3>AppLaunch Pro</h3>
    <p>Effortlessly design, build, and launch mobile apps with intuitive tools.</p>
    <a class="learn">Learn more →</a>
  </article>
  <article class="abs product" style="left:372px">
    <div class="ico" role="img" aria-label="Code window icon" style="background:linear-gradient(135deg,#5c8fe0,#f8b54a)"></div>
    <h3>CodeSync Connect</h3>
    <p>Collaborative platform for efficient teamwork and code synchronization.</p>
    <a class="learn">Learn more →</a>
  </article>
  <article class="abs product" style="left:609px">
    <div class="ico" role="img" aria-label="Interface design tools icon" style="background:linear-gradient(135deg,#f8a020,#7c80c6)"></div>
    <h3>UI/UX Ignite</h3>
    <p>Create engaging apps with stunning interfaces and seamless user experiences.</p>
    <a class="learn">Learn more →</a>
  </article>
  <article class="abs product" style="left:846px">
    <div class="ico" role="img" aria-label="Secure phone with lock icon" style="background:linear-gradient(135deg,#7c80c6,#f8b54a)"></div>
    <h3>AppShield Secure</h3>
    <p>Robust security solution for protecting apps from cyber threats.</p>
    <a class="learn">Learn more →</a>
  </article>

  <!-- why choose us -->
  <div class="abs why-art" role="img" aria-label="Illustration of a developer standing beside large phone screens and code panels"></div>
  <div class="abs eyebrow why-eyebrow">Essentials</div>
  <h2 class="abs h2 why-title">Why Choose Us?</h2>
  <p class="abs why-lead">Discover the advantages of partnering with us for your mobile app development needs.</p>
  <ul class="abs why-list">
    <li><svg width="18" height="18" viewBox="0 0 18 18"><circle cx="9" cy="9" r="9" fill="var(--orange)"/><path d="M5 9.3l2.6 2.5L13 6.5" stroke="#fff" stroke-width="2" fill="none" stroke-linecap="round"/></svg>Our experienced developers create tailored, high-quality apps</li>
    <li><svg width="18" height="18" viewBox="0 0 18 18"><circle cx="9" cy="9" r="9" fill="var(--orange)"/><path d="M5 9.3l2.6 2.5L13 6.5" stroke="#fff" stroke-width="2" fill="none" stroke-linecap="round"/></svg>Stay ahead with engaging, cutting-edge technology</li>
    <li><svg width="18" height="18" viewBox="0 0 18 18"><circle cx="9" cy="9" r="9" fill="var(--orange)"/><path d="M5 9.3l2.6 2.5L13 6.5" stroke="#fff" stroke-width="2" fill="none" stroke-linecap="round"/></svg>Flexible, timely, iterative development process</li>
    <li><svg width="18" height="18" viewBox="0 0 18 18"><circle cx="9" cy="9" r="9" fill="var(--orange)"/><path d="M5 9.3l2.6 2.5L13 6.5" stroke="#fff" stroke-width="2" fill="none" stroke-linecap="round"/></svg>From ideation to updates, we've got you covered</li>
  </ul>

  <!-- how it works -->
  <div class="abs eyebrow center how-eyebrow">Essentials</div>
  <h2 class="abs h2 center how-title">How It Work</h2>
  <svg class="abs how-path" viewBox="0 0 1200 200" aria-hidden="true">
    <path d="M245 27 H960 C1050 27 1075 60 1075 105 C1075 160 1030 196 960 196 H663" stroke="#d6d8e6" stroke-width="1.2" stroke-dasharray="4 4" fill="none"/>
  </svg>
  <div class="abs step" style="left:135px">
    <div class="ico"><span style="background:linear-gradient(135deg,#f8a020,#e5533d)"></span></div>
    <h3>Idea Exploration</h3>
    <p>Share your app concept<br>and goals with us</p>
  </div>
  <div class="abs step" style="left:373px">
    <div class="ico"><span style="background:linear-gradient(135deg,#4a7fd9,#f8a020)"></span></div>
    <h3>Development</h3>
    <p>We create a personalized plan<br>for your app's development</p>
  </div>
  <div class="abs step" style="left:608px">
    <div class="ico"><span style="background:linear-gradient(135deg,#2f9ff0,#f8a020)"></span></div>
    <h3>Design &amp; Refinement</h3>
    <p>We craft your app with the user<br>experience at the forefront.</p>
  </div>
  <div class="abs step" style="left:844px">
    <div class="ico"><span style="background:linear-gradient(135deg,#7c80c6,#e5533d)"></span></div>
    <h3>Testing &amp; Launch</h3>
    <p>Rigorous testing leads to a<br>successful app launch</p>
  </div>
  <a class="abs btn btn-apply-how">Apply Now</a>

  <!-- projects -->
  <div class="abs projects-band"></div>
  <div class="abs eyebrow projects-eyebrow">Projects</div>
  <h2 class="abs h2 projects-title">Featured Projects</h2>

  <article class="abs project" style="left:135px">
    <div class="shot" role="img" aria-label="EcoConnect app screens on a purple gradient" style="background:linear-gradient(135deg,#6a3fc9 0%,#8c79e6 45%,#e14a5a 80%,#2b2350 100%)"></div>
    <h3>EcoConnect</h3>
    <div class="tag">SUSTAINABILITY APP</div>
    <p>EcoConnect is an eco-conscious mobile</p>
    <p>app that fosters environmental awareness.</p>
    <a class="learn">Learn more about project →</a>
  </article>
  <article class="abs project" style="left:455px">
    <div class="shot" role="img" aria-label="HealthPulse mobile interface screens on blue" style="background:linear-gradient(135deg,#123a7a 0%,#2a5db8 50%,#cfe0f6 100%)"></div>
    <h3>HealthPulse</h3>
    <div class="tag">WELLNESS TRACKER</div>
    <p>HealthPulse is a comprehensive wellness</p>
    <p>tracker app that empowers users to monitor.</p>
    <a class="learn">Learn more about project →</a>
  </article>
  <article class="abs project" style="left:773px">
    <div class="shot" role="img" aria-label="Tourify360 travel app screens on dark plum" style="background:linear-gradient(135deg,#5a2e48 0%,#7b4566 45%,#e9e4ec 55%,#4c2940 100%)"></div>
    <h3>Tourify360</h3>
    <div class="tag">VIRTUAL TRAVEL COMPANION</div>
    <p>Tourify360 revolutionizes travel</p>
    <p>experiences through an immersive mobile app.</p>
    <a class="learn">Learn more about project →</a>
  </article>

  <!-- testimonials -->
  <div class="abs eyebrow center t-eyebrow">Testimonials</div>
  <h2 class="abs h2 center t-title">Our Clients Say</h2>

  <div class="abs quote" style="left:188px">
    <div class="stars">
      <svg width="96" height="18" viewBox="0 0 96 18"><g fill="var(--orange)"><path id="st" d="M9 0l2.6 5.6 6.1.7-4.5 4.2 1.2 6L9 13.5 3.6 16.5l1.2-6L.3 6.3l6.1-.7z"/><use href="#st" x="23"/><use href="#st" x="46"/><use href="#st" x="69"/><use href="#st" x="92" transform="translate(-15 0)"/></g></svg>
    </div>
    <div class="client" style="left:280px"><i></i>Midtown Grill</div>
    <blockquote>"Working with the mobile app development team was a game-changer for our business. Their expertise and attention to detail brought our app to life beyond our expectations."</blockquote>
    <div class="person" style="top:160px;left:18px"><i></i><div><b>Maya Ellison</b><span>Marketing Director</span></div></div>
  </div>

  <div class="abs quote" style="left:648px">
    <div class="stars">
      <svg width="96" height="18" viewBox="0 0 96 18"><g fill="var(--orange)"><path d="M9 0l2.6 5.6 6.1.7-4.5 4.2 1.2 6L9 13.5 3.6 16.5l1.2-6L.3 6.3l6.1-.7z"/><path transform="translate(23 0)" d="M9 0l2.6 5.6 6.1.7-4.5 4.2 1.2 6L9 13.5 3.6 16.5l1.2-6L.3 6.3l6.1-.7z"/><path transform="translate(46 0)" d="M9 0l2.6 5.6 6.1.7-4.5 4.2 1.2 6L9 13.5 3.6 16.5l1.2-6L.3 6.3l6.1-.7z"/><path transform="translate(69 0)" d="M9 0l2.6 5.6 6.1.7-4.5 4.2 1.2 6L9 13.5 3.6 16.5l1.2-6L.3 6.3l6.1-.7z"/></g></svg>
    </div>
    <div class="client" style="left:262px"><i style="background:#d94a3a;border-radius:2px"></i>Ridgeline</div>
    <blockquote>"The app developed by this team revolutionized our operations. Their dedication to delivering a seamless and efficient solution truly impressed us."</blockquote>
    <div class="person" style="top:160px;left:18px"><i></i><div><b>Peter Hollis</b><span>CEO</span></div></div>
  </div>

  <!-- call to action -->
  <div class="abs cta-band"></div>
  <div class="abs cta-box"></div>
  <div class="abs cta-gears" role="img" aria-label="Decorative orange and lavender gears"></div>
  <h2 class="abs cta-title">Ready To Transform <em>Your App Idea</em><br>Into Reality?</h2>
  <a class="abs btn btn-apply-cta">Apply Now</a>

  <!-- footer -->
  <div class="abs foot-brand">QuartzNook<small>WORKS</small></div>
  <p class="abs foot-about">Let's bring your vision to life. <a>Contact us today</a> and let our expertise in mobile app development turn your ideas into reality.</p>

  <h4 class="abs foot-h" style="left:506px">Quick links</h4>
  <ul class="abs foot-links">
    <li>About</li><li>Products</li><li>Projects</li><li>Contributions</li><li>News</li>
  </ul>

  <h4 class="abs foot-h" style="left:704px">Contact info</h4>
  <ul class="abs contact-list">
    <li><svg width="13" height="14" viewBox="0 0 24 24"><path d="M12 2a7 7 0 00-7 7c0 5 7 13 7 13s7-8 7-13a7 7 0 00-7-7zm0 9.5A2.5 2.5 0 1112 6.5a2.5 2.5 0 010 5z" fill="var(--orange)"/></svg>48 Larkfield Rd, Cary, NC 27511</li>
    <li><svg width="13" height="13" viewBox="0 0 24 24"><path d="M6.6 10.8a15 15 0 006.6 6.6l2.2-2.2a1 1 0 011-.25 11.4 11.4 0 003.6.57 1 1 0 011 1V20a1 1 0 01-1 1A17 17 0 013 4a1 1 0 011-1h3.5a1 1 0 011 1c0 1.25.2 2.45.57 3.57a1 1 0 01-.25 1z" fill="var(--orange)"/></svg>555-014-2276</li>
    <li><svg width="13" height="12" viewBox="0 0 24 20"><rect x="1" y="2" width="22" height="16" rx="2" fill="var(--orange)"/><path d="M2 4l10 7 10-7" stroke="#fff" stroke-width="2" fill="none"/></svg>hello@quartznook.com</li>
  </ul>

  <h4 class="abs foot-h" style="left:921px">Follow us</h4>
  <div class="abs socials">
    <span role="img" aria-label="Video channel"></span>
    <span role="img" aria-label="Professional network"></span>
    <span role="img" aria-label="Photo sharing"></span>
    <span role="img" aria-label="Social page"></span>
  </div>

  <a class="abs to-top" aria-label="Back to top">
    <svg width="16" height="18" viewBox="0 0 16 18"><path d="M8 17V2M2 8l6-6 6 6" stroke="#fff" stroke-width="2" fill="none" stroke-linecap="round"/></svg>
  </a>
  <div class="abs foot-rule"></div>
  <div class="abs center copyright">© 2023 All Rights Reserved | QuartzNook Works, LLC</div>
</div>
</body>
</html>
```